Skill Up Salary Up

Full Page
7.5 w x 10 h / 8 w x 10.75 h + .25" bleed
Full-Page Career Course Ad
Project Overview
• Goal: Create a visually attractive, modern, and uncluttered full-page magazine advertisement to list available career courses.
• Tone: Creative, professional, and attention-grabbing to prevent the reader from turning the page. The final design must prioritize readability.

Content Requirements
1. Header/Headline: Must be the primary focus. And grab peoples attention
2. Course Listing: A clear, well-organized list of the career courses.
________________________________________
Design & Aesthetic Directives
1. Layout & Readability (Crucial)
• The final ad must not look crowded or busy.
• Prioritize white space to make the text "breathe" and ensure the course list is easy to scan and read.
• Use a modern, clean, and professional typeface (font choice is critical for the aesthetic).
2. Visual Style
• Aim for a creative, modern, and fresh look. Avoid outdated or generic stock imagery/layouts.
3. Imagery/Graphic Element (Artist's Choice)
You have creative freedom regarding the main graphic element.
• Option A (Photography): Use a photo of a white male American with a collared shirt. The imagery should convey success, focus, or professional development.
• Option B (Vector/Illustration): Use a modern vector graphic, illustration, or abstract design. This could be used to symbolize growth, connection, or a career path.
The choice of graphic element is yours, but it must support the overall modern and uncrowded aesthetic.

Requirements
Must have
• Partial listing .. is part of the Harbor Lantern Course

```html
<!DOCTYPE html>
<html lang="en">
<head>
<meta charset="utf-8">
<title>Skill Up, Salary Up – Upcoming HLX Courses</title>
<link rel="stylesheet" href="https://fonts.googleapis.com/css2?family=Anton&family=Oswald:wght@600;700&family=Poppins:ital,wght@0,400;0,600;1,600&display=swap">
<style>
  :root {
    --blue-deep: #0a2f9e;
    --blue-mid: #1546d6;
    --blue-bright: #2a6df2;
    --ink-blue: #0b3cb4;
    --badge: #0a3aa8;
    --paper: #f6f6f6;
    --paper-edge: #e3e3e3;
    --ink: #1a1a1a;
    --white: #ffffff;
  }
  * { margin: 0; padding: 0; box-sizing: border-box; }
  html, body { width: 962px; height: 1200px; overflow: hidden; background: #ffffff; }
  .ad {
    position: relative; width: 962px; height: 1200px; overflow: hidden;
    background:
      radial-gradient(ellipse 70% 35% at 60% 22%, rgba(120,180,255,.45), transparent 70%),
      linear-gradient(180deg, var(--blue-mid) 0%, var(--blue-bright) 35%, var(--blue-mid) 70%, var(--blue-deep) 100%);
    font-family: "Poppins", sans-serif; color: var(--ink);
  }
  .kicker, .headline {
    position: absolute; left: 0; width: 100%; text-align: center; color: var(--white);
    font-family: "Anton", sans-serif; text-shadow: 0 3px 8px rgba(0,20,90,.45); line-height: 1;
  }
  .kicker { top: 58px; font-size: 54px; letter-spacing: .5px; }
  .headline { top: 122px; font-size: 82px; letter-spacing: 1px; }
  .pill {
    position: absolute; top: 238px; height: 43px; background: var(--white); border-radius: 10px;
    display: flex; align-items: center; justify-content: center;
    font-family: "Poppins", sans-serif; font-weight: 600; font-size: 18px; color: var(--ink-blue);
  }
  .pill--audience { left: 59px; width: 208px; }
  .pill--format { left: 288px; width: 277px; }
  .pill--aid { left: 588px; width: 317px; }
  .book {
    position: absolute; left: 59px; top: 362px; width: 846px; height: 535px;
    background: linear-gradient(90deg, var(--paper) 0%, #fff 45%, var(--paper-edge) 50%, #fff 55%, var(--paper) 100%);
    border-radius: 6px; box-shadow: 0 10px 24px rgba(0,20,80,.4);
  }
  .book::before {
    content: ""; position: absolute; left: 0; top: 0; bottom: 0; width: 6px;
    border-right: 1px solid #d6d6d6; border-radius: 6px 0 0 6px;
  }
  .course-title {
    position: absolute; font-family: "Oswald", sans-serif; font-weight: 700; font-size: 17px;
    color: var(--ink-blue); line-height: 20px;
  }
  .label { position: absolute; font-family: "Oswald", sans-serif; font-weight: 700; font-size: 11px; color: var(--ink-blue); }
  .lead { position: absolute; font-weight: 600; font-size: 11px; line-height: 14px; }
  .lead em { font-style: italic; }
  .list { position: absolute; list-style: none; font-size: 11px; line-height: 15px; }
  .list--arrow li::before { content: "➤ "; font-size: 8px; }
  .list--tick li::before { content: "✓ "; font-size: 10px; }
  .badge {
    position: absolute; width: 100px; background: var(--badge); border-radius: 12px; color: var(--white);
    font-family: "Anton", sans-serif; text-align: center; line-height: 1; padding-top: 8px;
    box-shadow: 0 2px 4px rgba(0,0,0,.2);
  }
  .badge__num { font-size: 26px; display: block; padding-bottom: 3px; border-bottom: 1px solid rgba(255,255,255,.7); margin: 0 14px 3px; }
  .badge__unit { font-size: 22px; display: block; }
  .badge__date { font-size: 19px; display: block; }
  .badge--tall { height: 93px; }
  .badge--short { height: 40px; padding-top: 9px; }
  .portrait { position: absolute; left: 297px; top: 791px; }
</style>
</head>
<body>
<main class="ad">
  <p class="kicker">SKILL UP, SALARY UP</p>
  <h1 class="headline">UPCOMING HLX COURSES</h1>

  <div class="pill pill--audience">MEN &amp; WOMEN</div>
  <div class="pill pill--format">IN-PERSON &amp; REMOTE</div>
  <div class="pill pill--aid">PARTIAL SCHOLORASHIPS</div>

  <section class="book">
    <!-- left page -->
    <h2 class="course-title" style="left:53px;top:44px;">Harbor Lantern Course</h2>
    <p class="lead" style="left:53px;top:70px;">Business Skills &amp; Knowledge to:</p>
    <ul class="list list--arrow" style="left:53px;top:90px;">
      <li>Impress your interviewer</li><li>Maximize Income</li><li>Start / Run Your Business</li>
    </ul>
    <p class="label" style="left:53px;top:144px;">Partial listing</p>
    <ul class="list list--tick" style="left:53px;top:159px;"><li>Computers</li><li>Marketing</li><li>Sales</li><li>Finance</li></ul>
    <ul class="list list--tick" style="left:154px;top:159px;"><li>Healthcare</li><li>Business</li><li>Strategy</li><li>Communication</li></ul>
    <ul class="list list--tick" style="left:286px;top:159px;"><li>LedgerPro</li><li>Investments</li><li>Real Estate</li><li>Accounting</li></ul>
    <div class="badge badge--tall" style="left:273px;top:50px;">
      <span class="badge__num">4-5</span><span class="badge__unit">MONTHS</span><span class="badge__date">NOV 2025</span>
    </div>

    <h2 class="course-title" style="left:53px;top:253px;">Software, Web &amp; Apps</h2>
    <p class="lead" style="left:53px;top:279px;"><em># 2 Best Tech Job</em><br>National Careers Review</p>
    <p class="lead" style="left:53px;top:314px;font-weight:400;">Job Opportunities</p>
    <ul class="list list--arrow" style="left:53px;top:330px;">
      <li>Computer Programmer</li><li>Software Developer/Mobile</li><li>Engineer Developer (Apps)</li>
    </ul>
    <p class="label" style="left:53px;top:382px;">Optional</p>
    <ul class="list list--tick" style="left:53px;top:397px;"><li>Bachelors in Prog. &amp;Tech.</li></ul>
    <div class="badge badge--short" style="left:273px;top:255px;"><span class="badge__date">NOV 2025</span></div>

    <!-- right page -->
    <h2 class="course-title" style="left:462px;top:44px;">Bookkeeping LedgerPro</h2>
    <p class="lead" style="left:462px;top:73px;">Train for a quality job<br>Manage your own books</p>
    <ul class="list list--arrow" style="left:462px;top:110px;">
      <li>Finance Management</li><li>Customer &amp; Vendor Mgmt.</li><li>Advanced Tools</li>
    </ul>
    <div class="badge badge--tall" style="left:670px;top:50px;">
      <span class="badge__num">05</span><span class="badge__unit">WEEKS</span><span class="badge__date">NOV 2025</span>
    </div>

    <h2 class="course-title" style="left:462px;top:192px;">IT Desktop &amp; Networking<br>Support</h2>
    <p class="lead" style="left:462px;top:241px;"><em>#2 Best Job</em><br>National Careers Review 2025</p>
    <ul class="list list--arrow" style="left:462px;top:272px;">
      <li>Impress your interviewer</li><li>Maximize Income</li><li>Start / Run Your Business</li>
    </ul>
    <p class="label" style="left:462px;top:326px;">Masters IT</p>
    <ul class="list list--tick" style="left:462px;top:341px;"><li>Desktop OS</li></ul>
    <ul class="list list--tick" style="left:553px;top:341px;"><li>Networks</li></ul>
    <ul class="list list--tick" style="left:644px;top:341px;"><li>Servers</li></ul>
    <ul class="list list--tick" style="left:722px;top:341px;"><li>Cloud</li></ul>
    <div class="badge badge--tall" style="left:670px;top:195px;">
      <span class="badge__num">07</span><span class="badge__unit">MONTHS</span><span class="badge__date">DEC 2025</span>
    </div>

    <h2 class="course-title" style="left:462px;top:396px;">Desktop Office- Computers</h2>
    <p class="label" style="left:462px;top:422px;">The New &nbsp;Job Prerequisite</p>
    <ul class="list list--tick" style="left:462px;top:436px;"><li>Sheets</li><li>Docs</li></ul>
    <ul class="list list--tick" style="left:553px;top:436px;"><li>Mail</li><li>Slides</li></ul>
    <p class="lead" style="left:462px;top:474px;">Computer lab available to<br>practice</p>
    <div class="badge badge--tall" style="left:670px;top:399px;">
      <span class="badge__num">05</span><span class="badge__unit">WEEKS</span><span class="badge__date">DEC 2025</span>
    </div>
  </section>

  <svg class="portrait" width="364" height="409" viewBox="0 0 364 409" role="img" aria-label="Photo of a smiling grey-haired man in a light collared shirt holding a tablet">
    <defs>
      <linearGradient id="portraitTone" x1="0" y1="0" x2="0" y2="1">
        <stop offset="0" stop-color="#9a8e86"/>
        <stop offset=".45" stop-color="#e4e1dc"/>
        <stop offset="1" stop-color="#cfcbc5"/>
      </linearGradient>
    </defs>
    <path d="M103 40 Q150 0 200 35 L208 118 L230 135 L320 165 Q350 185 364 409 L0 409 Q12 190 40 165 L120 135 L108 118 Z" fill="url(#portraitTone)"/>
  </svg>
</main>
</body>
</html>
```